ebook cover Lost At Holloway
Lost at Holloway
Creative Brief
Books
women - middle aged and older readers of cozy mysteries
The title Lost at Holloway should not be really big- not overpowering the page. It should not be dark or creepy. The words A Mabel Fenwick Mystery must be under it somewhere. The author Nora Pult should be at the bottom of the page. The background picture is a sunny,colorful, small Kansas town. Small town square, soft,colorful,nostalgic look. Square like Beyond Tomorrow Lane only set in 2011. No clock tower- but movie theatre @1950 - with Lumaro in neon pink vertically and theatre horizontally - theatre ending in "re" -library with white pillar on either side of front door with glass window--library across from theatre- if you can't do this give me a homey square with diagonal parking. DO NOT put anything violent in this and make sure the subtitle to Lost at Holloway is A Mabel Fenwick mystery. Give me a cover I could hand to a lady at church.

```html
<!DOCTYPE html>
<html lang="en">
<head>
<meta charset="utf-8">
<title>Lost At Holloway — A Mabel Fenwick Mystery</title>
<link rel="stylesheet" href="https://fonts.googleapis.com/css2?family=Bodoni+Moda:wght@400;500;600&family=Cormorant+Garamond:wght@500;600&display=swap">
<style>
  :root {
    --stage-top: #ffffff;
    --stage-bottom: #e4e4e6;
    --sky-gold: #f7d08a;
    --sky-peach: #f2a27a;
    --rose: #d9546a;
    --neon-pink: #ff5fa2;
    --brick: #8e3344;
    --plum: #4a1a2c;
    --title-white: #ffffff;
    --byline-cream: #fbf4ea;
    --rule: #f3e6d8;
  }
  * { margin: 0; padding: 0; box-sizing: border-box; }
  html, body {
    width: 1200px;
    height: 926px;
    overflow: hidden;
  }
  body {
    background: linear-gradient(to bottom, var(--stage-top) 0%, var(--stage-top) 45%, var(--stage-bottom) 100%);
    position: relative;
  }
  .book-cover {
    position: absolute;
    left: 279px;
    top: 50px;
    width: 605px;
    height: 841px;
    overflow: hidden;
    background: var(--plum);
    box-shadow: 0 4px 14px rgba(0,0,0,0.25);
  }
  .cover-scene {
    position: absolute;
    inset: 0;
    width: 100%;
    height: 100%;
  }
  .cover-text {
    position: absolute;
    inset: 0;
    text-align: center;
    color: var(--title-white);
    text-shadow: 0 1px 8px rgba(74,26,44,0.55);
  }
  .title {
    position: absolute;
    top: 118px;
    left: 0;
    right: 0;
    font-family: "Bodoni Moda", "Didot", serif;
    font-weight: 500;
    line-height: 0.98;
    letter-spacing: -0.5px;
  }
  .title-line { display: block; }
  .title-line--first { font-size: 92px; }
  .title-small { font-size: 56px; }
  .title-line--second { font-size: 80px; }
  .series-article {
    position: absolute;
    top: 560px;
    left: 0; right: 0;
    font-family: "Cormorant Garamond", "Times New Roman", serif;
    font-size: 24px;
    color: var(--byline-cream);
  }
  .series-name {
    position: absolute;
    top: 596px;
    left: 0; right: 0;
    font-family: "Cormorant Garamond", "Times New Roman", serif;
    font-weight: 600;
    font-size: 48px;
    color: var(--byline-cream);
  }
  .series-rules {
    position: absolute;
    top: 668px;
    left: 166px;
    width: 273px;
    height: 58px;
    border-top: 2px solid var(--rule);
    border-bottom: 1px solid rgba(243,230,216,0.6);
  }
  .series-label {
    position: absolute;
    top: 678px;
    left: 0; right: 0;
    font-family: "Cormorant Garamond", "Times New Roman", serif;
    font-size: 28px;
    letter-spacing: 18px;
    padding-left: 18px;
    color: var(--byline-cream);
  }
  .author {
    position: absolute;
    top: 770px;
    left: 0; right: 0;
    font-family: "Bodoni Moda", "Didot", serif;
    font-weight: 500;
    font-size: 30px;
    letter-spacing: 6px;
    color: var(--title-white);
  }
</style>
</head>
<body>
  <main class="book-cover">
    <svg class="cover-scene" viewBox="0 0 605 841" role="img" aria-label="Sunny small-town square with a 1950s movie theatre, vertical pink neon sign and marquee, and a pillared library across the street">
      <defs>
        <linearGradient id="sceneBase" x1="0" y1="0" x2="0" y2="1">
          <stop offset="0" stop-color="#f7d08a"/>
          <stop offset="0.4" stop-color="#f2a27a"/>
          <stop offset="0.72" stop-color="#c4566a"/>
          <stop offset="1" stop-color="#4a1a2c"/>
        </linearGradient>
        <radialGradient id="sunGlow" cx="0.85" cy="0.1" r="0.5">
          <stop offset="0" stop-color="#fff4d2" stop-opacity="0.9"/>
          <stop offset="1" stop-color="#f7d08a" stop-opacity="0"/>
        </radialGradient>
        <radialGradient id="neonGlow" cx="0.12" cy="0.48" r="0.4">
          <stop offset="0" stop-color="#ff5fa2" stop-opacity="0.65"/>
          <stop offset="1" stop-color="#d9546a" stop-opacity="0"/>
        </radialGradient>
      </defs>
      <rect width="605" height="841" fill="url(#sceneBase)"/>
      <rect width="605" height="841" fill="url(#sunGlow)"/>
      <rect width="605" height="841" fill="url(#neonGlow)"/>
    </svg>

    <div class="cover-text">
      <h1 class="title">
        <span class="title-line title-line--first">LOST <span class="title-small">AT</span></span>
        <span class="title-line title-line--second">HOLLOWAY</span>
      </h1>
      <p class="series-article">A</p>
      <p class="series-name">Mabel Fenwick</p>
      <div class="series-rules"></div>
      <p class="series-label">Mystery</p>
      <p class="author">NORA PULT</p>
    </div>
  </main>
</body>
</html>
```